Application for baby milk and water counter

We are building baby food app. Need to design main screen for tha app first so we can go forward to other secondary screens of the app

Food dashboard screen
Food dashboard screen is main page for view/edit food data

General vision
I see the app in pastel colors with some illustrations to make the app more in positive. You can influence from game Lantern Orchard. I see with smooth colors and gradients like in a game. Also need to have animations/transitions for each action. Each click should create smooth transition to new state. My idea is to build one dashboard screen for food which we can reuse it for other screens. So a lot of thinking should go into design stage to app appealing.

Food Dashboard
Current screen should show all the data about food intake of the baby. So here user should see

Milk How much food baby had in ml/oz. So there should be some kind of illustrated bottle or glass or smth that shows it is filled with that amount.

Add/Remove controls for food. Should be some kind of custom control for inputing amount to remove/add. I see it as a slider on the side of the bottle. User slides up or down and amount is added/removed.

Notification. So user should be aware how many hours/minutes left for next food intake. This is optional field, so consider it could be disabled. So no empty space should be on a screen. There should be human readable text. Something like. 1:30 minutes left for next intake. Maybe could be some custom made icons to illustrate that it is next food intake.

Burped: User should have ability to how much baby burped. This amount is integer value. So it could be “Baby burped 2 times today”. So again here I see some custom made/icon to illustrate how many times baby burped and amount next to it. I see changing the value just by tapping, but I don’t know how to edit if user tapped accidentally more than it should be. So TBD here.

Date and time: Dashboard should show for which date it is viewing/editing data. Should be able to change it, so user can add/edit data for yesterday. Don’t want to see here calendar on a screen so need to come up with nice design decision.

Water: User should have ability to view/edit water intake of the baby, but water is secondary information so it should be smaller than milk, or come up with some other idea how to show the water. I see to have same controls for water like for milk. Water intake is optional it can be disabled by the user.

Target Market(s)

For just became mothers

Font styles to use
Sans Serif

Colors
0094D4
00A9DD
6FCCEA
C7EBF8
E9F6FB
FFC000
F8CF3A
FAE287
FDF2CF
FEFAEE
E54698
E96AAD
F1A4CE
F9D9EA
FCEFF6

Requirements
Must have
• Ilustrations or playfull icons for show information

```html
<!DOCTYPE html>
<html lang="en">
<head>
<meta charset="utf-8">
<title>Daily Milk &amp; Water Plan</title>
<link href="https://fonts.googleapis.com/css2?family=Outfit:wght@300;400;500;700&display=swap" rel="stylesheet">
<style>
  :root{
    --blue-900:#0094D4; --blue-700:#00A9DD; --blue-500:#6FCCEA; --blue-200:#C7EBF8; --blue-50:#E9F6FB;
    --yellow-900:#FFC000; --yellow-700:#F8CF3A; --yellow-500:#FAE287; --yellow-200:#FDF2CF; --yellow-50:#FEFAEE;
    --pink-900:#E54698; --pink-700:#E96AAD; --pink-500:#F1A4CE; --pink-200:#F9D9EA;
    --ink:#111111; --ink-soft:#3a3a3a; --muted:#555; --pill:#F3F3F5; --panel:#F4F4F6; --page:#E9E9E9; --white:#fff;
  }
  *{box-sizing:border-box;margin:0;padding:0}
  html,body{width:1200px;height:1200px;overflow:hidden;background:var(--page);font-family:'Outfit',sans-serif;color:var(--ink)}
  .screen{position:absolute;left:343px;top:44px;width:604px;height:1308px;background:var(--white);border-radius:64px;overflow:hidden;transform:scale(.85);transform-origin:top left}
  .abs{position:absolute}
  .title{left:37px;top:82px;font-size:47px;line-height:56px;font-weight:400;letter-spacing:-.3px}
  .title b{font-weight:700}
  .avatar{left:474px;top:94px;width:92px;height:92px;border-radius:50%;background:var(--yellow-500)}
  .month{left:40px;top:211px;font-size:26px;font-weight:400;display:flex;align-items:center;gap:12px}
  .day{top:267px;width:97px;height:155px;border-radius:49px;background:var(--pill);text-align:center;color:var(--ink-soft)}
  .day .num{display:block;margin-top:34px;font-size:47px;line-height:52px;font-weight:400}
  .day .name{display:block;margin-top:6px;font-size:16px;color:var(--muted)}
  .day.is-active{background:var(--pink-900);width:102px;height:163px;border-radius:51px;color:var(--white)}
  .day.is-active .num{font-weight:500;color:var(--white)}
  .day.is-active .name{color:var(--white)}
  .day.is-active::after{content:"";display:block;width:30px;height:3px;border-radius:2px;background:var(--pink-200);margin:14px auto 0}
  .panel{left:0;top:436px;width:604px;height:872px}
  .bottle{border:6px solid var(--white);border-radius:52px;overflow:hidden;box-shadow:0 2px 10px rgba(0,0,0,.03)}
  .bottle-milk{left:70px;top:516px;width:214px;height:524px;background:var(--yellow-50)}
  .bottle-water{left:323px;top:768px;width:214px;height:272px;background:var(--blue-50)}
  .fill{position:absolute;left:0;right:0;bottom:0}
  .icon-badge{position:absolute;left:50%;transform:translateX(-50%);width:88px;height:88px;border-radius:50%;display:flex;align-items:center;justify-content:center}
  .bottle-label{position:absolute;left:0;right:0;text-align:center;font-size:19px;font-weight:500;color:var(--ink-soft)}
  .tick{position:absolute;width:20px;height:2px}
  .scale-label{font-size:16px;font-weight:500;color:var(--ink-soft)}
  .slider{left:155px;top:708px;width:42px;height:83px;border-radius:21px;background:var(--white);box-shadow:0 2px 8px rgba(0,0,0,.08)}
  .tooltip{left:209px;top:733px;width:62px;height:32px;border-radius:6px;background:var(--ink);color:var(--white);font-size:16px;font-weight:500;display:flex;align-items:center;justify-content:center}
  .tooltip::before{content:"";position:absolute;left:-6px;top:10px;border-style:solid;border-width:6px 6px 6px 0;border-color:transparent var(--ink) transparent transparent}
  .burped{left:194px;top:1067px;width:215px;height:59px;border-radius:30px;background:var(--ink);color:var(--white);font-size:20px;font-weight:300;display:flex;align-items:center;justify-content:center;letter-spacing:.3px}
  .reminder{left:0;top:1146px;width:604px;height:162px}
  .reminder-icon{left:73px;top:1183px;width:100px;height:100px;border-radius:50%;background:var(--white);display:flex;align-items:center;justify-content:center}
  .reminder-text{left:205px;top:1216px;font-size:25px;font-weight:500;color:var(--white);letter-spacing:.3px}
</style>
</head>
<body>
<main class="screen">
  <h1 class="abs title">Your Daily <b>Milk</b><br><b>&amp; Water</b>&nbsp; Plan</h1>
  <div class="abs avatar" role="img" aria-label="Parent profile avatar"></div>

  <div class="abs month">November 2022
    <svg width="18" height="12" viewBox="0 0 18 12"><path d="M2 2l7 7 7-7" fill="none" stroke="#111" stroke-width="2.6" stroke-linecap="round"/></svg>
  </div>

  <div class="abs day" style="left:37px"><span class="num">22</span><span class="name">Fri</span></div>
  <div class="abs day" style="left:144px"><span class="num">23</span><span class="name">Sat</span></div>
  <div class="abs day is-active" style="left:251px"><span class="num">24</span><span class="name">Sun</span></div>
  <div class="abs day" style="left:364px"><span class="num">24</span><span class="name">Mon</span></div>
  <div class="abs day" style="left:472px"><span class="num">26</span><span class="name">Tue</span></div>

  <svg class="abs panel" viewBox="0 0 604 872" preserveAspectRatio="none">
    <path d="M0 60 Q0 0 60 0 H100 Q115 0 118 16 Q124 37 150 37 H455 Q480 37 487 16 Q492 0 510 0 H540 Q604 0 604 60 V872 H0Z" fill="var(--panel)"/>
  </svg>

  <span class="abs scale-label" style="left:21px;top:555px">200ml</span>
  <div class="abs bottle bottle-milk">
    <svg class="fill" width="202" height="290" viewBox="0 0 202 290" preserveAspectRatio="none">
      <defs><linearGradient id="milkGrad" x1="0" y1="0" x2="0" y2="1"><stop offset="0" stop-color="#FAE287"/><stop offset="1" stop-color="#FFC000"/></linearGradient></defs>
      <path d="M0 6 Q50 0 100 4 T202 2 V290 H0Z" fill="url(#milkGrad)"/>
    </svg>
    <div class="icon-badge" style="top:26px;background:var(--yellow-200)">
      <svg width="26" height="48" viewBox="0 0 26 48" fill="none" stroke="var(--yellow-700)" stroke-width="1.6"><rect x="8" y="1" width="10" height="5" rx="1"/><path d="M9 6v6l-6 8v24a3 3 0 003 3h14a3 3 0 003-3V20l-6-8V6"/><path d="M6 38v3"/></svg>
    </div>
    <div class="bottle-label" style="top:124px">Milk Bottle</div>
    <div class="tick" style="left:0;top:44px;background:var(--yellow-700)"></div>
    <div class="tick" style="left:0;top:103px;background:var(--yellow-700)"></div>
    <div class="tick" style="left:0;top:163px;background:var(--yellow-700)"></div>
    <div class="tick" style="left:0;top:222px;background:var(--yellow-700)"></div>
    <div class="tick" style="left:0;top:285px;background:var(--yellow-700)"></div>
    <div class="tick" style="left:0;top:345px;background:var(--yellow-700)"></div>
    <div class="tick" style="left:0;top:405px;background:var(--yellow-700)"></div>
    <div class="tick" style="left:0;top:464px;background:var(--yellow-700)"></div>
  </div>

  <div class="abs slider">
    <svg width="42" height="83" viewBox="0 0 42 83" fill="none" stroke="#555" stroke-width="1.4" stroke-linecap="round">
      <path d="M15 17l6-6 6 6"/><path d="M15 66l6 6 6-6"/>
      <path d="M17 35h8M13 40h16M13 44h16M17 49h8"/>
    </svg>
  </div>
  <div class="abs tooltip">100ml</div>

  <div class="abs bottle bottle-water">
    <svg class="fill" width="202" height="126" viewBox="0 0 202 126" preserveAspectRatio="none">
      <defs><linearGradient id="waterGrad" x1="0" y1="0" x2="0" y2="1"><stop offset="0" stop-color="#6FCCEA"/><stop offset="1" stop-color="#0094D4"/></linearGradient></defs>
      <path d="M0 6 Q60 12 120 6 T202 2 V126 H0Z" fill="url(#waterGrad)"/>
    </svg>
    <div class="icon-badge" style="top:16px;background:var(--blue-200)">
      <svg width="22" height="46" viewBox="0 0 22 46" fill="none" stroke="var(--blue-700)" stroke-width="1.6"><rect x="7" y="1" width="8" height="5" rx="1"/><path d="M8 6v5c0 4-6 8-6 14v16a3 3 0 003 3h12a3 3 0 003-3V25c0-6-6-10-6-14V6"/></svg>
    </div>
    <div class="bottle-label" style="top:116px">Water Bottle</div>
    <div class="tick" style="right:0;top:30px;background:var(--blue-700)"></div>
    <div class="tick" style="right:0;top:91px;background:var(--blue-700)"></div>
    <div class="tick" style="right:0;top:151px;background:var(--blue-700)"></div>
    <div class="tick" style="right:0;top:211px;background:var(--blue-700)"></div>
  </div>
  <span class="abs scale-label" style="left:535px;top:794px">100ml</span>

  <div class="abs burped">2 times burped</div>

  <svg class="abs reminder" viewBox="0 0 604 162" preserveAspectRatio="none">
    <path d="M0 80 Q0 2 80 2 H210 Q228 2 245 10 Q262 17 280 17 H330 Q348 17 365 10 Q382 2 400 2 H524 Q604 2 604 80 V162 H0Z" fill="var(--pink-700)"/>
  </svg>
  <div class="abs reminder-icon">
    <svg width="56" height="56" viewBox="0 0 56 56" fill="none" stroke="var(--pink-700)" stroke-width="4" stroke-linecap="round" stroke-linejoin="round">
      <path d="M46 32A20 20 0 1 1 28 8"/>
      <path d="M26 18v12l8 7"/>
      <path d="M41 42l6-10 8 6"/>
    </svg>
  </div>
  <div class="abs reminder-text">2 hours left for next intake</div>
</main>
</body>
</html>
```